we do all sorts of cleaning however bookings are limited!
why not chose the right cleaners for you!
pressure cleaning, window cleaning, office, end of lease clean, accommodation, industrial and commercial cleaning and house cleaning

Logo Text

Bright Nest Cleaning Service

```html
<!DOCTYPE html>
<html lang="en">
<head>
<meta charset="utf-8">
<title>Bright Nest Cleaning Service – Business Card</title>
<link href="https://fonts.googleapis.com/css2?family=Montserrat:wght@400;600;700&display=swap" rel="stylesheet">
<style>
  :root {
    --backdrop: #676b6f;
    --card: #ffffff;
    --blue: #03adef;
    --green: #8cc63f;
    --ink: #243447;
  }
  * { margin: 0; padding: 0; box-sizing: border-box; }
  html, body {
    width: 1200px; height: 1167px; overflow: hidden;
    background: var(--backdrop);
    font-family: "Montserrat", Arial, sans-serif;
  }
  .card {
    position: absolute; left: 260px; width: 679px; height: 388px;
    background: var(--card); overflow: hidden;
  }
  .card--front { top: 124px; }
  .card--back { top: 638px; }

  .band { position: absolute; left: 0; width: 100%; }
  .band--top { top: 0; height: 57px; background: linear-gradient(180deg, var(--blue) 0%, var(--blue) 55%, var(--green) 100%); }
  .band--bottom { bottom: 0; height: 60px; background: linear-gradient(180deg, var(--green) 0%, var(--blue) 45%, var(--blue) 100%); }
  .card--back .band--bottom { background: linear-gradient(180deg, var(--blue) 0%, var(--green) 45%, var(--green) 100%); }

  .brand { position: absolute; color: var(--blue); font-weight: 700; text-align: center; line-height: 1; }
  .brand__name { display: block; }
  .brand__tagline { display: block; letter-spacing: 0.04em; }
  .card--front .brand { left: 0; width: 100%; top: 150px; }
  .card--front .brand__name { font-size: 64px; }
  .card--front .brand__tagline { font-size: 22px; margin-top: 20px; }
  .card--back .brand { left: 338px; width: 290px; top: 70px; }
  .card--back .brand__name { font-size: 38px; }
  .card--back .brand__tagline { font-size: 13px; margin-top: 8px; }

  .holder__bar { position: absolute; left: 0; top: 83px; width: 25px; height: 53px; background: var(--blue); }
  .holder__name { position: absolute; left: 34px; top: 82px; font-size: 32px; font-weight: 600; color: var(--green); line-height: 1; }
  .holder__title { position: absolute; left: 34px; top: 113px; font-size: 15px; font-weight: 400; color: var(--ink); line-height: 1; }
  .divider { position: absolute; left: 24px; top: 184px; width: 623px; height: 3px; background: var(--green); }

  .contact { position: absolute; list-style: none; color: var(--ink); font-size: 19px; font-weight: 600; }
  .contact__item { position: absolute; display: flex; align-items: center; white-space: nowrap; line-height: 1; }
  .contact__icon { width: 20px; height: 20px; margin-right: 9px; flex: none; }
  .contact--lines { left: 43px; top: 0; }
  .address { position: absolute; left: 420px; top: 213px; display: flex; color: var(--ink); font-size: 19px; font-weight: 600; line-height: 29px; font-style: normal; }
  .address .contact__icon { margin-right: 13px; margin-top: 3px; }
</style>
</head>
<body>

<section class="card card--front">
  <div class="band band--top" role="img" aria-label="Blue and green decorative band along the top edge"></div>
  <div class="brand">
    <span class="brand__name">Bright Nest</span>
    <span class="brand__tagline">CLEANING SERVICE</span>
  </div>
  <div class="band band--bottom" role="img" aria-label="Green and blue decorative band along the bottom edge"></div>
</section>

<section class="card card--back">
  <div class="holder__bar"></div>
  <p class="holder__name">Your Name</p>
  <p class="holder__title">Title</p>

  <div class="brand">
    <span class="brand__name">Bright Nest</span>
    <span class="brand__tagline">CLEANING SERVICE</span>
  </div>

  <div class="divider"></div>

  <ul class="contact contact--lines">
    <li class="contact__item" style="top:219px">
      <svg class="contact__icon" viewBox="0 0 20 20" aria-hidden="true"><circle cx="10" cy="10" r="10" fill="var(--blue)"/><path d="M7 5.5 C6 6 5.5 7 6 8.5 C7 11 9 13 11.5 14 C13 14.5 14 14 14.5 13 L13 11.5 L11.5 12.2 C10 11.5 8.5 10 7.8 8.5 L8.5 7 Z" fill="#fff"/></svg>
      012 345 6789
    </li>
    <li class="contact__item" style="top:257px">
      <svg class="contact__icon" viewBox="0 0 20 20" aria-hidden="true"><circle cx="10" cy="10" r="10" fill="var(--blue)"/><rect x="5.5" y="7" width="9" height="6.5" fill="#fff"/><path d="M5.5 7 L10 10.5 L14.5 7" stroke="var(--blue)" stroke-width="1" fill="none"/></svg>
      info@website.com
    </li>
    <li class="contact__item" style="top:294px">
      <svg class="contact__icon" viewBox="0 0 20 20" aria-hidden="true"><circle cx="10" cy="10" r="8.5" fill="none" stroke="var(--blue)" stroke-width="2"/><ellipse cx="10" cy="10" rx="3.5" ry="8.5" fill="none" stroke="var(--blue)" stroke-width="1.5"/><path d="M2 10 H18 M3.5 6 H16.5 M3.5 14 H16.5" stroke="var(--blue)" stroke-width="1.3"/></svg>
      www.website.com
    </li>
  </ul>

  <address class="address">
    <svg class="contact__icon" viewBox="0 0 20 20" aria-hidden="true"><circle cx="10" cy="10" r="10" fill="var(--blue)"/><path d="M10 4.5 C7.5 4.5 6 6.3 6 8.3 C6 11 10 15.5 10 15.5 C10 15.5 14 11 14 8.3 C14 6.3 12.5 4.5 10 4.5 Z" fill="#fff"/><circle cx="10" cy="8.4" r="1.6" fill="var(--blue)"/></svg>
    <span>0000 Street<br>Address<br>0000</span>
  </address>

  <div class="band band--bottom" role="img" aria-label="Blue and green decorative band along the bottom edge"></div>
</section>

</body>
</html>
```